Emergency Management Consulting Flyer

Company name: Stone Harbor Emergency Management

I am looking for a postcard design for my emergency management consulting business. I'm looking for something that has some colors and is double sided, on side with the information on services provided and the other side with the contact information. For the main side I'm looking for the following:

How prepared are you?

Services Provided:
Healthcare Preparedness
EOC Support
Emergency Planning
Mitigation Planning
Business Continuity
Disaster Response
Training and Exercises
Project Management
And more

Affordable for small and large organizations
Stand-by contracts available

On the back side, I'm looking for Contact Us section.

Overall I'm looking for something a bit more modern and need to have at least one disaster photo. If you have questions please message me.

Target Market(s)

Government, Healthcare Facilities, Businesses

Industry/Entity Type

Consulting

Requirements
Must have
• Disaster Picture, modern looking
• For the main side I'm looking for the following:
• How prepared are you?
• Services Provided:
• Healthcare Preparedness
• EOC Support
• Emergency Planning
• Mitigation Planning
• Business Continuity
• Disaster Response
• Training and Exercises
• Project Management
• And more
• Affordable for small and large organizations
• Stand-by contracts available

```html
<!DOCTYPE html>
<html lang="en">
<head>
<meta charset="utf-8">
<title>Stone Harbor Emergency Management – Postcard</title>
<link href="https://fonts.googleapis.com/css2?family=Montserrat:wght@300;400;800&display=swap" rel="stylesheet">
<style>
  :root {
    --blue: #0b72c6;
    --blue-dark: #0a5fa8;
    --red: #d7362c;
    --red-dark: #8e1f19;
    --grey-light: #f3f3f3;
    --grey: #d9d9d9;
    --ink: #1f3550;
    --brand: #3a3a3a;
    --accent: #f08a1c;
    --white: #ffffff;
    --page: #e9e9e9;
  }
  * { margin: 0; padding: 0; box-sizing: border-box; }
  html, body { width: 817px; height: 1200px; overflow: hidden; background: var(--page); }
  body { position: relative; font-family: "Montserrat", sans-serif; }

  .postcard {
    position: absolute; left: 68px; width: 840px; height: 648px;
    transform: scale(0.81); transform-origin: top left;
    overflow: hidden; background: var(--white);
    box-shadow: 0 4px 14px rgba(0,0,0,.18);
  }
  .postcard--front { top: 40px; }
  .postcard--back { top: 622px; }
  .postcard__shapes { position: absolute; inset: 0; width: 840px; height: 648px; }

  .brand { position: absolute; display: flex; flex-direction: column; align-items: center; }
  .brand__dot { width: 70px; height: 70px; border-radius: 50%; background: var(--accent); margin-bottom: 22px; }
  .brand__name { font-weight: 800; color: var(--brand); text-transform: uppercase; text-align: center; line-height: 1.15; letter-spacing: .5px; }
  .postcard--front .brand { left: 20px; top: 60px; width: 255px; }
  .postcard--front .brand__name { font-size: 24px; }
  .postcard--back .brand { left: 40px; top: 565px; flex-direction: row; align-items: center; gap: 14px; }
  .postcard--back .brand__dot { width: 46px; height: 46px; margin: 0; }
  .postcard--back .brand__name { font-size: 20px; text-align: left; }

  .headline { position: absolute; color: var(--white); font-weight: 800; }
  .postcard--front .headline { right: 20px; top: 462px; font-size: 44px; letter-spacing: .5px; }
  .tagline { position: absolute; right: 22px; top: 534px; color: var(--white); font-weight: 300; font-size: 27px; letter-spacing: .6px; }
  .contact-row { position: absolute; right: 20px; top: 597px; color: var(--ink); font-weight: 400; font-size: 25px; letter-spacing: .5px; display: flex; align-items: center; gap: 16px; }
  .contact-row__divider { width: 2px; height: 38px; background: var(--ink); }

  .postcard--back .headline { left: 26px; top: 22px; font-size: 37px; line-height: 1.25; }
  .services { position: absolute; left: 27px; top: 128px; color: var(--white); }
  .services__title { font-size: 17px; font-weight: 300; margin-bottom: 5px; }
  .services__list { list-style: none; padding-left: 24px; }
  .services__item { font-size: 18px; font-weight: 400; line-height: 23px; position: relative; padding-left: 18px; }
  .services__item--check::before {
    content: ""; position: absolute; left: 0; top: 7px; width: 9px; height: 9px;
    border: 1.5px solid var(--red); border-radius: 50%;
  }
  .back-contact { position: absolute; left: 25px; top: 400px; color: var(--white); font-weight: 300; font-size: 25px; letter-spacing: .5px; line-height: 31px; }
  .back-contact__web { margin-top: 20px; }
  .contact-icon { position: absolute; left: 300px; top: 400px; width: 120px; height: 110px; }
</style>
</head>
<body>

<section class="postcard postcard--front">
  <svg class="postcard__shapes" viewBox="0 0 840 648" aria-hidden="false">
    <defs>
      <linearGradient id="panelGrey" x1="0" y1="0" x2="0" y2="1">
        <stop offset="0" stop-color="#dcdcdc"/>
        <stop offset="1" stop-color="#f7f7f7"/>
      </linearGradient>
      <linearGradient id="damTones" x1="0" y1="0" x2="1" y2="1">
        <stop offset="0" stop-color="#7fa9b8"/>
        <stop offset=".45" stop-color="#a9a59a"/>
        <stop offset="1" stop-color="#5d8a3c"/>
      </linearGradient>
      <linearGradient id="floodTones" x1="0" y1="0" x2="1" y2="1">
        <stop offset="0" stop-color="#6f7356"/>
        <stop offset="1" stop-color="#3f5a34"/>
      </linearGradient>
    </defs>
    <rect width="840" height="648" fill="url(#panelGrey)"/>
    <polygon points="505,0 840,0 840,453 245,453" fill="url(#damTones)" role="img" aria-label="Photo of a large concrete dam holding back a mountain reservoir"/>
    <polygon points="0,283 330,283 105,648 0,648" fill="url(#floodTones)" role="img" aria-label="Aerial photo of a town flooded by river water"/>
    <polygon points="432,0 450,0 270,283 252,283" fill="var(--blue)"/>
    <polygon points="205,453 840,453 840,525 165,525" fill="var(--blue)"/>
    <polygon points="165,525 840,525 840,577 135,577" fill="var(--red)"/>
    <polygon points="135,577 840,577 840,648 105,648" fill="url(#panelGrey)"/>
  </svg>

  <div class="brand">
    <div class="brand__dot"></div>
    <div class="brand__name">Stone Harbor<br>Emergency Management</div>
  </div>

  <h1 class="headline">How prepared are you?</h1>
  <p class="tagline">Affordable for small and large organizations</p>
  <div class="contact-row">
    <span>Contact Us:&nbsp; 000 000 000</span>
    <span class="contact-row__divider"></span>
    <span>www.yourwebsite.com</span>
  </div>
</section>

<section class="postcard postcard--back">
  <svg class="postcard__shapes" viewBox="0 0 840 648">
    <defs>
      <linearGradient id="footGrey" x1="0" y1="0" x2="0" y2="1">
        <stop offset="0" stop-color="#d6d6d6"/>
        <stop offset="1" stop-color="#f2f2f2"/>
      </linearGradient>
    </defs>
    <polygon points="0,0 382,0 475,548 0,548" fill="var(--blue)"/>
    <polygon points="0,548 475,548 490,648 0,648" fill="url(#footGrey)"/>
    <polygon points="470,528 492,528 486,548" fill="var(--red-dark)"/>
    <polygon points="0,380 465,380 492,528 0,528" fill="var(--red)"/>
    <rect x="678" y="53" width="114" height="92" fill="none" stroke="#cfcfcf" stroke-width="2"/>
    <g stroke="#d2d2d2" stroke-width="2">
      <line x1="536" y1="291" x2="792" y2="291"/>
      <line x1="536" y1="330" x2="792" y2="330"/>
      <line x1="536" y1="369" x2="792" y2="369"/>
      <line x1="536" y1="408" x2="792" y2="408"/>
      <line x1="536" y1="447" x2="792" y2="447"/>
    </g>
  </svg>

  <h2 class="headline">How prepared<br>are you?</h2>

  <div class="services">
    <p class="services__title">Services Provided:</p>
    <ul class="services__list">
      <li class="services__item services__item--check">Healthcare Preparedness</li>
      <li class="services__item services__item--check">EOC Support</li>
      <li class="services__item services__item--check">Emergency Planning</li>
      <li class="services__item services__item--check">Mitigation Planning</li>
      <li class="services__item services__item--check">Business Continuity</li>
      <li class="services__item services__item--check">Disaster Response</li>
      <li class="services__item services__item--check">Training and Exercises</li>
      <li class="services__item services__item--check">Project Management</li>
      <li class="services__item">And more</li>
    </ul>
  </div>

  <div class="back-contact">
    <p>Contact Us:</p>
    <p>000 000 000</p>
    <p class="back-contact__web">www.yourwebsite.com</p>
  </div>

  <svg class="contact-icon" viewBox="0 0 120 110" aria-hidden="true">
    <path d="M38 4 C16 4 4 16 4 30 C4 42 13 51 26 54 L24 66 L38 56 C58 56 72 45 72 30 C72 16 60 4 38 4 Z" fill="none" stroke="var(--white)" stroke-width="6" stroke-linejoin="round"/>
    <circle cx="24" cy="30" r="5" fill="var(--white)"/>
    <circle cx="38" cy="30" r="5" fill="var(--white)"/>
    <circle cx="52" cy="30" r="5" fill="var(--white)"/>
    <path d="M96 40 C104 38 112 44 112 52 C110 72 88 96 58 104 C48 106 40 100 40 92 L54 84 C58 82 62 84 64 88 C74 84 88 70 92 60 C88 58 86 54 88 50 Z" fill="var(--white)"/>
  </svg>

  <div class="brand">
    <div class="brand__dot"></div>
    <div class="brand__name">Stone Harbor<br>Emergency Management</div>
  </div>
</section>

</body>
</html>
```